Handyman home maintenance postcard

We would like the postcard to state what we do : Painting, plumbing, electrical, flooring, carpentry, drywall, fencing, windows and more. We would also like our promotion to state : First four hours of work is only $299. Additional hours are 25% off our regular rate of $110 an hour. Rate includes two expert handymen working to complete your job.

Target Market(s)

30-75

Industry/Entity Type

Home maintenance

```html
<!DOCTYPE html>
<html lang="en">
<head>
<meta charset="utf-8">
<title>Steadfast Handyman Services – Postcard</title>
<link rel="stylesheet" href="https://fonts.googleapis.com/css2?family=Poppins:wght@400;500;600;700;800;900&family=Oswald:wght@500;600&display=swap">
<style>
  :root{
    --orange:#f5870e;
    --orange-deep:#ec6d05;
    --red:#e02020;
    --ink:#111111;
    --white:#ffffff;
    --stage:#e9e7e7;
    --stamp:#e4e4e4;
    --rule:#333333;
  }
  *{box-sizing:border-box;margin:0;padding:0}
  html,body{width:1200px;height:2400px;overflow:hidden}
  body{background:var(--stage);font-family:"Poppins",sans-serif;color:var(--ink);position:relative}

  .card{position:absolute;left:123px;width:955px;height:636px;background:var(--white);overflow:hidden;box-shadow:0 2px 6px rgba(0,0,0,.12)}
  .card--front{top:524px}
  .card--back{top:1240px}

  .brand{position:absolute;display:flex;align-items:center;gap:10px}
  .brand__dot{width:34px;height:34px;border-radius:50%;background:var(--orange);flex:0 0 34px}
  .brand__name{font-weight:700;font-size:24px;line-height:1.05;color:var(--ink);letter-spacing:-.3px;white-space:nowrap}
  .brand--back{left:538px;top:40px;gap:8px}
  .brand--back .brand__dot{width:28px;height:28px;flex:0 0 28px}
  .brand--back .brand__name{font-size:20px}

  /* front */
  .front__photo{position:absolute;left:506px;top:0;width:449px;height:636px;background:radial-gradient(ellipse at 55% 45%,#a89684 0%,#6e5c4c 55%,#3e3229 100%)}
  .headline{position:absolute;left:32px;top:108px;width:420px}
  .headline__top{font-weight:800;font-size:94px;line-height:.95;color:var(--orange);letter-spacing:-2px}
  .headline__mid{font-weight:800;font-size:71px;line-height:.95;color:var(--ink);letter-spacing:-1px}
  .headline__sub{font-weight:500;font-size:29px;letter-spacing:.2em;line-height:1.1;margin-top:2px;white-space:nowrap}
  .tagbar{position:absolute;left:0;top:294px;width:458px;height:31px;background:var(--ink);color:var(--white);font-weight:700;font-size:17px;letter-spacing:.06em;display:flex;align-items:center;padding-left:32px;white-space:nowrap}
  .tagbar em{font-style:normal;color:var(--orange);margin-right:6px}
  .discount{position:absolute;left:30px;top:336px;font-weight:800;font-size:64px;line-height:.98;letter-spacing:-1px}
  .discount span{display:block;color:var(--orange-deep)}
  .discount__box{position:absolute;left:175px;top:343px;width:277px;height:112px;background:var(--red);color:var(--white);font-weight:700;font-size:34px;line-height:1.03;padding:4px 0 0 14px}
  .rate{position:absolute;left:32px;top:466px;width:420px;height:40px;display:flex}
  .rate__label{flex:0 0 263px;background:var(--ink);color:var(--white);border-radius:6px 0 0 6px;font-weight:600;font-size:17px;display:flex;align-items:center;padding-left:11px;white-space:nowrap}
  .rate__label small{font-size:11px;font-weight:500;margin-left:5px}
  .rate__price{flex:1;background:var(--orange-deep);color:var(--white);border-radius:0 6px 6px 0;font-weight:700;font-size:28px;display:flex;align-items:center;justify-content:center}
  .includes{position:absolute;left:32px;top:514px}
  .includes__title{font-weight:700;font-size:23px;color:var(--orange-deep);line-height:1.1}
  .includes__text{font-weight:500;font-size:12.5px}
  .call{position:absolute;display:flex;align-items:center;gap:12px;white-space:nowrap}
  .call__label{font-weight:700;font-size:24px;color:var(--orange)}
  .call__label b{color:var(--red);font-weight:700}
  .call__number{font-weight:700;font-size:36px;letter-spacing:-.5px}
  .card--front .call{left:30px;top:565px}
  .offer{position:absolute;left:478px;top:286px;width:280px;height:125px}
  .offer__text{position:absolute;left:22px;top:38px;color:var(--white);font-weight:800;font-size:17px;line-height:.95;transform:rotate(-3deg)}
  .offer__text .hl{color:#ffd21a}
  .offer__text small{display:block;font-size:9px;font-weight:500;margin-top:2px}
  .offer__price{position:absolute;left:120px;top:18px;color:var(--white);font-family:"Oswald",sans-serif;font-weight:600;font-size:66px;line-height:1;transform:rotate(-3deg)}
  .offer__price sup{font-size:30px;vertical-align:top;position:relative;top:6px}

  /* back */
  .back__panel{position:absolute;left:0;top:0;width:523px;height:636px;background:linear-gradient(180deg,var(--orange) 0%,var(--orange-deep) 100%)}
  .about{position:absolute;left:32px;top:22px;width:475px}
  .section-title{font-weight:700;font-size:30px;line-height:1.15;color:var(--ink)}
  .section-title span{color:var(--white)}
  .about p{font-size:12.2px;line-height:1.33;color:var(--white);margin-top:4px}
  .gallery{position:absolute;left:0;top:146px;width:536px;height:182px;background:var(--ink);display:flex;gap:10px;padding:10px 31px 11px 32px}
  .gallery__item{flex:1;background:linear-gradient(135deg,#6b7889 0%,#3c4552 60%,#23282f 100%)}
  .services{position:absolute;left:38px;top:330px;width:470px}
  .services__grid{display:flex;margin-top:6px}
  .services__col{flex:1;display:flex;flex-direction:column;align-items:center;gap:14px;border-right:2px dashed rgba(255,255,255,.85);padding:2px 0}
  .services__col:last-child{border-right:none}
  .svc{display:flex;flex-direction:column;align-items:center;gap:2px;color:var(--white);font-weight:600;font-size:13.5px}
  .svc svg{width:24px;height:24px}
  .values{position:absolute;left:0;top:499px;width:523px;height:137px;background:var(--ink);padding:14px 0 0 32px}
  .values__row{display:flex;gap:24px}
  .value{display:flex;gap:7px;color:var(--white);font-weight:700;font-size:13.5px;line-height:1.2}
  .value svg{width:12px;height:12px;flex:0 0 12px;margin-top:3px}
  .card--back .call{left:32px;top:576px}
  .card--back .call__label b{color:var(--orange)}
  .card--back .call__number{color:var(--white)}
  .stamp{position:absolute;left:822px;top:32px;width:103px;height:123px;background:var(--stamp)}
  .address-line{position:absolute;left:595px;width:330px;height:1px;background:var(--rule)}
</style>
</head>
<body>

<section class="card card--front">
  <div class="brand" style="left:32px;top:40px">
    <span class="brand__dot"></span>
    <span class="brand__name">Steadfast Handyman<br>Services</span>
  </div>

  <h1 class="headline">
    <div class="headline__top">TRUSTED</div>
    <div class="headline__mid">HANDYMAN</div>
    <div class="headline__sub">&amp; REPAIR SERVICES</div>
  </h1>

  <div class="tagbar"><em>YOUR EXPERT GO-TO</em> FOR HOME REPAIRS</div>

  <div class="discount">25%<span>OFF</span></div>
  <div class="discount__box">ON OUR<br>ADDITIONAL<br>HOURS</div>

  <div class="rate">
    <div class="rate__label">OUR REGULAR RATE <small>(AN HOUR)</small></div>
    <div class="rate__price">$110</div>
  </div>

  <div class="includes">
    <div class="includes__title">Rate includes</div>
    <div class="includes__text">two expert handymen working to complete your job.</div>
  </div>

  <div class="call">
    <span class="call__label">Call us <b>Now!</b></span>
    <svg width="28" height="28" viewBox="0 0 28 28"><circle cx="14" cy="14" r="14" fill="#111"/><path d="M10 7.5l2.3 3.2-1.4 1.6c.8 1.8 2.2 3.3 4 4.1l1.6-1.4 3.2 2.3-1.1 2.6c-5.6-.3-10.2-4.9-10.5-10.5z" fill="#fff"/></svg>
    <span class="call__number">555 014 2290</span>
  </div>

  <div class="front__photo" role="img" aria-label="Photo of a smiling handyman in a plaid shirt, apron and tool belt in a workshop"></div>

  <div class="offer">
    <svg width="280" height="125" viewBox="0 0 280 125">
      <defs><linearGradient id="offerFill" x1="0" x2="1"><stop offset="0" stop-color="#e8251a"/><stop offset="1" stop-color="#f57a0a"/></linearGradient></defs>
      <polygon points="2,30 276,2 248,104 6,122" fill="#fff"/>
      <polygon points="10,34 266,9 241,97 12,114" fill="url(#offerFill)"/>
    </svg>
    <div class="offer__text">FIRST<br><span class="hl">4 HOURS</span><br>OF WORK<small>IS ONLY</small></div>
    <div class="offer__price"><sup>$</sup>299</div>
  </div>
</section>

<section class="card card--back">
  <div class="back__panel"></div>

  <div class="about">
    <h2 class="section-title">Who <span>We Are?</span></h2>
    <p>Steadfast Handyman Services strives to be your go-to for home repairs. We have many years of experience in all facets of home repair and maintenance. Whether you are looking to repair that running toilet, replace that tired looking floor or give your home's exterior or interior a fresh new color, we can get it done for you. On time, neatly and at a reasonable price.</p>
  </div>

  <div class="gallery">
    <div class="gallery__item" role="img" aria-label="Photo of hands sanding a wooden board"></div>
    <div class="gallery__item" role="img" aria-label="Photo of a plumber fitting a water filter"></div>
    <div class="gallery__item" role="img" aria-label="Photo of an electrician working on a fuse panel"></div>
  </div>

  <div class="services">
    <h2 class="section-title">What <span>We Do?</span></h2>
    <div class="services__grid">
      <div class="services__col">
        <div class="svc"><svg viewBox="0 0 24 24"><circle cx="12" cy="12" r="12" fill="#111"/><path d="M7 8h8v3H7zM11 11h1.5v6H11z" fill="#fff"/></svg>Painting</div>
        <div class="svc"><svg viewBox="0 0 24 24"><circle cx="12" cy="12" r="12" fill="#111"/><path d="M7 9h10v3H7zM11 12h2v5h-2z" fill="#fff"/></svg>Plumbing</div>
      </div>
      <div class="services__col">
        <div class="svc"><svg viewBox="0 0 24 24"><circle cx="12" cy="12" r="12" fill="#111"/><path d="M13 5l-5 8h4l-1 6 5-8h-4z" fill="#fff"/></svg>Electrical</div>
        <div class="svc"><svg viewBox="0 0 24 24"><circle cx="12" cy="12" r="12" fill="#111"/><path d="M7 15h10v2H7zM9 9h6v5H9z" fill="#fff"/></svg>Flooring</div>
      </div>
      <div class="services__col">
        <div class="svc"><svg viewBox="0 0 24 24"><circle cx="12" cy="12" r="12" fill="#111"/><path d="M7 16l8-8 2 2-8 8zM14 7h4v2h-4z" fill="#fff"/></svg>Carpentry</div>
        <div class="svc"><svg viewBox="0 0 24 24"><circle cx="12" cy="12" r="12" fill="#111"/><path d="M7 7h10v10H7z" fill="#fff"/><path d="M7 10.5h10M7 13.5h10M12 7v3.5M9.5 10.5v3M14.5 10.5v3M12 13.5V17" stroke="#111" stroke-width="1"/></svg>Drywall</div>
      </div>
      <div class="services__col">
        <div class="svc"><svg viewBox="0 0 24 24"><circle cx="12" cy="12" r="12" fill="#111"/><path d="M8 7h2v10H8zM14 7h2v10h-2zM6 10h12v1.5H6zM6 13h12v1.5H6z" fill="#fff"/></svg>Fencing</div>
        <div class="svc"><svg viewBox="0 0 24 24"><circle cx="12" cy="12" r="12" fill="#111"/><path d="M7 7h10v10H7z" fill="#fff"/><path d="M12 7v10M7 12h10" stroke="#111" stroke-width="1.5"/></svg>Windows</div>
      </div>
    </div>
  </div>

  <div class="values">
    <div class="values__row">
      <div class="value"><svg viewBox="0 0 12 12"><circle cx="6" cy="6" r="6" fill="#f5870e"/><path d="M3 6l2 2 4-4" stroke="#fff" stroke-width="1.5" fill="none"/></svg>20+ YEARS OF<br>EXPERIENCE</div>
      <div class="value"><svg viewBox="0 0 12 12"><circle cx="6" cy="6" r="6" fill="#f5870e"/><path d="M3 6l2 2 4-4" stroke="#fff" stroke-width="1.5" fill="none"/></svg>RELIABLE &amp;<br>QUALITY SERVICE</div>
      <div class="value"><svg viewBox="0 0 12 12"><circle cx="6" cy="6" r="6" fill="#f5870e"/><path d="M3 6l2 2 4-4" stroke="#fff" stroke-width="1.5" fill="none"/></svg>SKILLED &amp;<br>TRAINED PERSONEL</div>
    </div>
  </div>

  <div class="call">
    <span class="call__label">Call us <b>Now!</b></span>
    <svg width="28" height="28" viewBox="0 0 28 28"><circle cx="14" cy="14" r="14" fill="#f5870e"/><path d="M10 7.5l2.3 3.2-1.4 1.6c.8 1.8 2.2 3.3 4 4.1l1.6-1.4 3.2 2.3-1.1 2.6c-5.6-.3-10.2-4.9-10.5-10.5z" fill="#111"/></svg>
    <span class="call__number">555 014 2290</span>
  </div>

  <div class="brand brand--back">
    <span class="brand__dot"></span>
    <span class="brand__name">Steadfast Handyman<br>Services</span>
  </div>
  <div class="stamp"></div>
  <div class="address-line" style="top:258px"></div>
  <div class="address-line" style="top:297px"></div>
  <div class="address-line" style="top:339px"></div>
  <div class="address-line" style="top:384px"></div>
</section>

</body>
</html>
```